Billboard design for dentist that sees only children

I own a 12' x 25' digital billboard and I need help with billboard design. My wife is a general dentist that only sees children and is very passionate about giving them a quality dental experience . She has a great reputation in town. Obviously with a billboard there can't be a lot of reading. Maybe something that shows safety, love, experience and children. I am completely open to your ideas. In addition I have other businesses that also need billboard design so this could lead to more work. If you go to Maplecovedental.com under the about section you will find more information about the practice and our phone number. Attached is our logo which could be changed and content specs for the digital billboard. Happy Designing!!

Target Market(s)

Parents with children

Colors

Designer to choose colors to be used in the design.

Requirements
Must have
• Must attract attention and be nice to look at.
Nice to have
• Probably should have children in the picture ..... Maybe
Should not have
• If I see something I don't like I will let you know

```html
<!DOCTYPE html>
<html lang="en">
<head>
<meta charset="utf-8">
<title>Maple Cove Dental – Billboard</title>
<link href="https://fonts.googleapis.com/css2?family=Montserrat:wght@500;600;700&family=Arimo:wght@400&display=swap" rel="stylesheet">
<style>
  :root{
    --page:#e6e9ec;
    --sky-pale:#a8cfe6;
    --sky-mid:#2fa3dd;
    --navy:#0d59a6;
    --navy-deep:#0a4a8f;
    --gap:#eef4f8;
    --ink:#111111;
    --red:#e3262b;
    --white:#ffffff;
    --teal:#2a6f8a;
    --tag:#2f8fcf;
  }
  *{margin:0;padding:0;box-sizing:border-box}
  html,body{width:1200px;height:1000px;overflow:hidden;background:var(--page)}
  .billboard{position:absolute;left:40px;top:253px;width:1120px;height:493px;overflow:hidden;box-shadow:0 4px 14px rgba(0,0,0,.25)}
  .billboard-art{position:absolute;inset:0;width:100%;height:100%}
  .brand{position:absolute;left:22px;top:26px;display:flex;align-items:center;gap:14px;font-family:"Montserrat",sans-serif}
  .brand-dot{width:74px;height:74px;border-radius:50%;background:var(--teal);flex:none}
  .brand-text{display:flex;flex-direction:column;align-items:flex-end}
  .brand-name{font-weight:600;font-size:40px;line-height:1;color:var(--teal)}
  .brand-tagline{font-weight:500;font-size:21px;line-height:1.2;color:var(--tag);margin-top:4px}
  .line{position:absolute;font-family:"Montserrat",sans-serif;white-space:nowrap;text-align:right}
  .headline{top:62px;right:76px;font-size:37px;font-weight:700;letter-spacing:2px;color:var(--ink)}
  .headline-accent{top:124px;right:20px;font-size:31px;font-weight:600;color:var(--red);text-shadow:0 0 3px #fff,0 0 2px #fff}
  .subline{top:220px;right:19px;font-size:30px;font-weight:600;color:var(--ink);text-shadow:0 0 3px #fff,0 0 2px #fff}
  .subline-accent{top:280px;right:36px;font-size:33px;font-weight:700;letter-spacing:.5px;color:var(--red);text-shadow:0 0 3px #fff,0 0 2px #fff}
  .contact{position:absolute;right:28px;display:flex;align-items:center;gap:20px;font-family:"Arimo",sans-serif;color:var(--white);white-space:nowrap}
  .contact-phone{top:354px;font-size:38px}
  .contact-mail{top:406px;font-size:35px}
  .contact svg{width:40px;height:30px;flex:none}
</style>
</head>
<body>
<main class="billboard">
  <svg class="billboard-art" viewBox="0 0 1120 493" preserveAspectRatio="none">
    <defs>
      <radialGradient id="photoTone" cx=".28" cy=".52" r=".62">
        <stop offset="0" stop-color="#c98f6e"/>
        <stop offset=".3" stop-color="#d9a487"/>
        <stop offset=".55" stop-color="#b8544a"/>
        <stop offset=".8" stop-color="#7e9d4a"/>
        <stop offset="1" stop-color="#4d7a30"/>
      </radialGradient>
      <radialGradient id="brandGlow" cx=".5" cy=".5" r=".5">
        <stop offset="0" stop-color="#ffffff" stop-opacity=".95"/>
        <stop offset=".7" stop-color="#ffffff" stop-opacity=".8"/>
        <stop offset="1" stop-color="#ffffff" stop-opacity="0"/>
      </radialGradient>
    </defs>
    <rect class="photo" role="img" aria-label="Photo of smiling children lying in a circle on grass, making binoculars with their hands" width="1120" height="493" fill="url(#photoTone)"/>
    <ellipse cx="250" cy="70" rx="300" ry="85" fill="url(#brandGlow)"/>
    <!-- light backing so gaps between bands read as thin light lines -->
    <polygon points="683,0 1120,0 1120,493 375,493" fill="var(--gap)"/>
    <!-- top stripe band -->
    <polygon points="683,0 1120,0 1120,30 664,30" fill="var(--sky-pale)"/>
    <polygon points="930,0 990,0 975,30 915,30" fill="var(--sky-mid)"/>
    <polygon points="1040,0 1120,0 1120,30 1025,30" fill="var(--navy)"/>
    <!-- message panels -->
    <polygon points="661,36 1120,36 1120,190 562,190" fill="var(--sky-pale)"/>
    <polygon points="562,196 1120,196 1120,346 465,346" fill="var(--sky-mid)"/>
    <polygon points="465,352 1120,352 1120,463 393,463" fill="var(--navy)"/>
    <!-- bottom stripe band -->
    <polygon points="393,468 1120,468 1120,493 375,493" fill="var(--sky-pale)"/>
    <polygon points="640,468 700,468 688,493 628,493" fill="var(--sky-mid)"/>
    <polygon points="900,468 1120,468 1120,493 888,493" fill="var(--navy-deep)"/>
  </svg>

  <div class="brand">
    <span class="brand-dot"></span>
    <div class="brand-text">
      <span class="brand-name">Maple Cove Dental</span>
      <span class="brand-tagline">general dentistry for children</span>
    </div>
  </div>

  <p class="line headline">Provide quality,</p>
  <p class="line headline-accent">Loving Care To Our Patients</p>
  <p class="line subline">Using State Of The Art Equipment</p>
  <p class="line subline-accent">And Advanced Techniques</p>

  <p class="contact contact-phone">555.014.2290
    <svg viewBox="0 0 40 30" aria-hidden="true"><path d="M4 12c0-6 32-6 32 0v3h-8v-3c-4-2-12-2-16 0v3H4z" fill="#fff"/><path d="M12 14h16l4 12H8z" fill="#fff"/><circle cx="20" cy="20" r="3.5" fill="#0d59a6"/></svg>
  </p>
  <p class="contact contact-mail">maplecovedds@example.com
    <svg viewBox="0 0 40 30" aria-hidden="true"><rect x="3" y="4" width="34" height="22" rx="2" fill="#fff"/><path d="M5 7l15 11 15-11M5 24l11-9M35 24l-11-9" stroke="#0d59a6" stroke-width="2" fill="none"/></svg>
  </p>
</main>
</body>
</html>
```